Business Cards Needed For Veterinary Business

Looking for a business card design for a veterinary blood bank. We would like it to be clean and professional on appearance but still warm and inviting. We would like to utilize our logo and similar coloring. We will use our phone number, email, website, employee name, employee title.

We do not want a bunch of animated animal photos but do not need the style to be as clinical as a laboratory or human medical procedure office.

We are looking for some creative ideas to choose from so that we can generate a standout professional business card for our management team to utilize.

Target Market(s)

professionals

Industry/Entity Type

veterinary

Contact Information for Business Card

employee name, employee title, phone number, website URL, email

Font styles to use
Sans Serif

Colors
0054AA
0677BA
7BADD7
CADEEF
E8F1F8
EB3D1F
EC4F4E
F09395
F8D3D4
FCEDEE

Requirements
Nice to have
• creative design
Should not have
• animated photos

```html
<!DOCTYPE html>
<html lang="en">
<head>
<meta charset="utf-8">
<title>Cedar Animal Blood Bank – Business Card</title>
<link href="https://fonts.googleapis.com/css2?family=Montserrat:wght@600;700&family=Poppins:wght@400;500;600&display=swap" rel="stylesheet">
<style>
  :root {
    --stage: #858585;
    --card-white: #ffffff;
    --brand-red: #ec1c24;
    --brand-blue: #0d4f91;
    --ink-blue: #12468c;
    --white: #ffffff;
  }
  * { margin: 0; padding: 0; box-sizing: border-box; }
  html, body {
    width: 1093px; height: 1200px; overflow: hidden;
    background: var(--stage);
  }
  .canvas { position: relative; width: 1093px; height: 1200px; }

  .card { position: absolute; left: 264px; border-radius: 24px; overflow: hidden; }

  /* Front */
  .card--front { top: 226px; width: 578px; height: 356px; background: var(--card-white); }
  .person { position: absolute; left: 26px; top: 79px; }
  .person__name {
    font-family: "Montserrat", sans-serif; font-weight: 700;
    font-size: 22px; line-height: 1; color: var(--brand-red); letter-spacing: -0.2px;
  }
  .person__title {
    font-family: "Poppins", sans-serif; font-weight: 400;
    font-size: 16px; line-height: 1.2; color: var(--ink-blue); margin-top: 1px;
  }
  .contact { position: absolute; left: 26px; top: 205px; list-style: none; }
  .contact__item {
    display: flex; align-items: center; height: 21px;
    font-family: "Poppins", sans-serif; font-size: 16.5px; color: var(--ink-blue);
  }
  .contact__icon { width: 15px; height: 15px; margin-right: 8px; flex: none; }
  .contact__accent { color: var(--brand-red); }

  .brand-front { position: absolute; left: 310px; top: 40px; width: 250px; text-align: center; }
  .brand-front__dot {
    width: 190px; height: 190px; border-radius: 50%;
    background: var(--brand-red); margin: 0 auto;
  }
  .brand-front__name {
    margin-top: 18px;
    font-family: "Poppins", sans-serif; font-weight: 600;
    font-size: 17px; color: var(--brand-red);
  }

  /* Back */
  .card--back { top: 621px; width: 583px; height: 355px; background: var(--brand-blue); }
  .lockup {
    position: absolute; left: 108px; top: 112px;
    display: flex; align-items: center;
  }
  .lockup__dot {
    width: 92px; height: 92px; border-radius: 50%;
    background: var(--brand-red); flex: none; margin-right: 18px;
  }
  .lockup__name {
    font-family: "Montserrat", sans-serif; font-weight: 700;
    font-size: 30px; line-height: 1.12; color: var(--white);
  }
</style>
</head>
<body>
<main class="canvas">

  <section class="card card--front" aria-label="Business card front">
    <div class="person">
      <h1 class="person__name">DANIEL HARTLEY</h1>
      <p class="person__title">Managing Director</p>
    </div>

    <ul class="contact">
      <li class="contact__item">
        <svg class="contact__icon" viewBox="0 0 16 16" aria-hidden="true">
          <path fill="#ec1c24" d="M3.6 1.2l2.3 2.6-1.2 1.7c.9 2.1 2.6 3.9 4.8 4.8l1.7-1.2 2.6 2.3-1.3 2.3C7.2 13.6 2.4 8.8 1.3 3.5z"/>
          <path fill="none" stroke="#ec1c24" stroke-width="1.2" d="M9.5 1.5a5 5 0 0 1 5 5M9.5 4a2.5 2.5 0 0 1 2.5 2.5"/>
        </svg>
        055-987 654 321
      </li>
      <li class="contact__item">
        <svg class="contact__icon" viewBox="0 0 16 16" aria-hidden="true">
          <rect x="0.5" y="3" width="15" height="10" fill="#ec1c24"/>
          <path fill="none" stroke="#fff" stroke-width="1.2" d="M1 3.5l7 5.5 7-5.5M1 12.5l5-4.5M15 12.5l-5-4.5"/>
        </svg>
        hello@cedarbank.com
      </li>
      <li class="contact__item">
        <svg class="contact__icon" viewBox="0 0 16 16" aria-hidden="true">
          <g fill="none" stroke="#ec1c24" stroke-width="1.2">
            <circle cx="8" cy="8" r="6.8"/>
            <ellipse cx="8" cy="8" rx="3" ry="6.8"/>
            <path d="M1.2 8h13.6M2.2 4.6h11.6M2.2 11.4h11.6"/>
          </g>
        </svg>
        www.<span class="contact__accent">cedarbloodbank</span>.com
      </li>
    </ul>

    <div class="brand-front">
      <div class="brand-front__dot"></div>
      <p class="brand-front__name">Cedar Animal Blood Bank</p>
    </div>
  </section>

  <section class="card card--back" aria-label="Business card back">
    <div class="lockup">
      <div class="lockup__dot"></div>
      <p class="lockup__name">Cedar Animal<br>Blood Bank</p>
    </div>
  </section>

</main>
</body>
</html>
```